engaging mobile application to encourage lifestyle change

We need an App that will help people get from Bold 4 Bloom. A weight loss program based on realistic and healthy lifestyle modifications. By learning portion control, healthy food choices, and with the encouragement to get moving.
We would like the design to be gender neutral but must be fun.
The final design must be easy to use and useful to our clients.

Target Market(s)

Health, Wellbeing, Weightloss

Industry/Entity Type

Weight

Font styles to use
Sans Serif

Requirements
Must have
• Hydration log, Weigh-ins with fat %, Food log, Location of meetings,lectures and weigh-ins, list of restaurants that comply with B4B, Fitness plan, Mall walk maps, daily motivational message.

```html
<!DOCTYPE html>
<html lang="en">
<head>
<meta charset="utf-8">
<title>Bold 4 Bloom – Hydration Log</title>
<link href="https://fonts.googleapis.com/css2?family=Raleway:wght@300;400;500;600;700&display=swap" rel="stylesheet">
<style>
  :root{
    --header-dark:#1f2420;
    --header-mid:#3b4a36;
    --header-light:#7f9a6e;
    --tab-active:#ffffff;
    --tab-idle:rgba(255,255,255,0.55);
    --ink:#1d1d1f;
    --muted:#8e9296;
    --rule:#dcdfe2;
    --track:#eeeff1;
    --accent:#5cc8f5;
    --cta:#ff8a6e;
    --paper:#ffffff;
  }
  *{box-sizing:border-box;margin:0;padding:0}
  html,body{width:692px;height:1200px;overflow:hidden;background:var(--paper);font-family:"Raleway",sans-serif;color:var(--ink)}
  .screen{position:relative;width:692px;height:1200px;background:var(--paper)}
  .header{position:absolute;left:0;top:0;width:692px;height:142px;
    background:linear-gradient(100deg,var(--header-dark) 0%,var(--header-dark) 30%,var(--header-mid) 55%,var(--header-light) 100%)}
  .header-band{position:absolute;left:240px;right:0;bottom:0;height:5px;background:rgba(200,200,200,0.55)}
  .status-bar{position:absolute;left:0;top:0;width:692px;height:44px;color:#fff;font-size:19px;font-weight:500}
  .carrier{position:absolute;left:22px;top:12px;display:flex;align-items:center;gap:6px}
  .clock{position:absolute;left:0;right:0;top:12px;text-align:center;font-weight:600}
  .battery{position:absolute;right:18px;top:12px;display:flex;align-items:center;gap:10px}
  .tabs{position:absolute;left:0;top:58px;width:692px;height:70px;display:flex}
  .tab{flex:1;display:flex;align-items:center;justify-content:center;gap:14px;position:relative}
  .tab + .tab::before{content:"";position:absolute;left:0;top:10px;height:50px;width:1px;background:rgba(255,255,255,0.3)}
  .tab-text{display:flex;flex-direction:column;line-height:1}
  .tab-kicker{font-size:13px;font-weight:500;letter-spacing:.2px;margin-bottom:6px}
  .tab-title{font-size:27px;font-weight:400}
  .tab.is-active{color:var(--tab-active)}
  .tab.is-idle{color:var(--tab-idle)}
  .tab.is-idle .tab-kicker{align-self:center}
  .goal{position:absolute;left:0;right:0;top:214px;text-align:center}
  .goal-title{font-size:29px;font-weight:500;letter-spacing:.3px}
  .goal-rule{width:312px;height:1px;background:var(--rule);margin:18px auto 16px}
  .goal-progress{font-size:22px;font-weight:400;color:#a4a8ac}
  .slider{position:absolute;left:79px;top:378px;width:536px;height:12px}
  .slider-track{position:absolute;inset:3px 0;border-radius:4px;background:var(--track)}
  .slider-fill{position:absolute;left:0;top:3px;height:6px;width:410px;border-radius:4px;background:var(--accent)}
  .slider-knob{position:absolute;left:394px;top:-11px;width:34px;height:34px;border-radius:50%;background:var(--accent)}
  .stats{position:absolute;left:43px;top:542px;width:605px;list-style:none}
  .stat{display:flex;justify-content:space-between;align-items:center;height:116px;padding:50px 14px 0 12px;border-bottom:2px solid var(--rule)}
  .stat:first-child{height:58px;padding-top:0}
  .stat-label{font-size:20px;font-weight:400;color:var(--muted)}
  .stat-value{font-size:27px;font-weight:500;color:var(--ink)}
  .cta{position:absolute;left:148px;top:975px;width:411px;height:70px;border-radius:35px;background:var(--cta);
    color:#fff;font-size:22px;font-weight:700;letter-spacing:.5px;display:flex;align-items:center;justify-content:center;border:none}
</style>
</head>
<body>
<main class="screen">
  <header class="header" role="img" aria-label="Blurred photo of fresh green herbs on a dark kitchen surface">
    <div class="header-band"></div>

    <div class="status-bar">
      <div class="carrier">
        <svg width="64" height="14" viewBox="0 0 64 14" aria-hidden="true">
          <circle cx="6" cy="7" r="5.5" fill="#fff"/><circle cx="19" cy="7" r="5.5" fill="#fff"/><circle cx="32" cy="7" r="5.5" fill="#fff"/>
          <circle cx="45" cy="7" r="5" fill="none" stroke="#fff" stroke-width="1.2"/><circle cx="58" cy="7" r="5" fill="none" stroke="#fff" stroke-width="1.2"/>
        </svg>
        <span>NOVA</span>
        <svg width="22" height="16" viewBox="0 0 22 16" aria-hidden="true">
          <path d="M11 15 L7.5 11 A5 5 0 0 1 14.5 11 Z" fill="#fff"/>
          <path d="M4.5 8 A9.5 9.5 0 0 1 17.5 8" stroke="#fff" stroke-width="2.2" fill="none"/>
          <path d="M1.5 4.8 A14 14 0 0 1 20.5 4.8" stroke="#fff" stroke-width="2.2" fill="none"/>
        </svg>
      </div>
      <div class="clock">4:21 PM</div>
      <div class="battery">
        <svg width="12" height="20" viewBox="0 0 12 20" aria-hidden="true">
          <path d="M1 5 L10 14 L6 18 V2 L10 6 L1 15" stroke="rgba(255,255,255,0.8)" stroke-width="1.4" fill="none"/>
        </svg>
        <span>100%</span>
        <svg width="44" height="18" viewBox="0 0 44 18" aria-hidden="true">
          <rect x="1" y="1" width="38" height="16" rx="3" fill="none" stroke="#fff" stroke-width="1.4"/>
          <rect x="3" y="3" width="34" height="12" rx="1.5" fill="#fff"/>
          <rect x="40.5" y="6" width="2.5" height="6" rx="1" fill="#fff"/>
        </svg>
      </div>
    </div>

    <nav class="tabs">
      <div class="tab is-active">
        <svg width="18" height="46" viewBox="0 0 18 46" aria-hidden="true" fill="#fff">
          <circle cx="9" cy="4.5" r="4"/>
          <path d="M3 10 H15 L17 24 H14 L13 45 H10 L9 30 L8 45 H5 L4 24 H1 Z"/>
        </svg>
        <div class="tab-text"><span class="tab-kicker">HYDRATION</span><span class="tab-title">LOG</span></div>
      </div>
      <div class="tab is-idle">
        <svg width="26" height="32" viewBox="0 0 26 32" aria-hidden="true" fill="rgba(255,255,255,0.45)">
          <rect x="4" y="0" width="6" height="4" rx="1"/>
          <path d="M3 6 H11 V10 L14 14 V31 H0 V14 L3 10 Z"/>
          <rect x="16" y="18" width="10" height="13" rx="2"/>
        </svg>
        <div class="tab-text"><span class="tab-kicker">FOOD</span><span class="tab-title">LOG</span></div>
      </div>
      <div class="tab is-idle">
        <svg width="24" height="30" viewBox="0 0 24 30" aria-hidden="true" fill="rgba(255,255,255,0.45)">
          <path d="M5 1 H19 V10 A7 7 0 0 1 5 10 Z"/>
          <path d="M5 4 H1 V8 A5 5 0 0 0 5 12" stroke="rgba(255,255,255,0.45)" stroke-width="2" fill="none"/>
          <path d="M19 4 H23 V8 A5 5 0 0 1 19 12" stroke="rgba(255,255,255,0.45)" stroke-width="2" fill="none"/>
          <rect x="10" y="16" width="4" height="7"/>
          <rect x="6" y="23" width="12" height="5" rx="1"/>
        </svg>
        <div class="tab-text"><span class="tab-kicker">WEIGH IN</span><span class="tab-title">FAT %</span></div>
      </div>
    </nav>
  </header>

  <section class="goal">
    <h1 class="goal-title">YOUR GOAL</h1>
    <div class="goal-rule"></div>
    <p class="goal-progress">4000 ml out of 5500ml</p>
  </section>

  <div class="slider" aria-label="Hydration progress">
    <div class="slider-track"></div>
    <div class="slider-fill"></div>
    <div class="slider-knob"></div>
  </div>

  <ul class="stats">
    <li class="stat"><span class="stat-label">Last Drink</span><span class="stat-value">200 ml</span></li>
    <li class="stat"><span class="stat-label">Next Drink</span><span class="stat-value">10:05 pm</span></li>
    <li class="stat"><span class="stat-label">Average Consumption</span><span class="stat-value">5500 ml</span></li>
  </ul>

  <button class="cta">FINISH STEP</button>
</main>
</body>
</html>
```